Tarvel Plumbing Solutions

This is for my new plumbing company, I have attached an example of what I’m going for but want it to look better.

Target Market(s)

Home owners, real estate, etc.

Industry/Entity Type

Plumbing

Font styles to use
Other font styles liked:
• As per my logo and other examples uploaded

Colors

Designer to choose colors to be used in the design.

Requirements
Must have
• Must include my logo provided and similar to my flyer I have attached but better

```html
<!DOCTYPE html>
<html lang="en">
<head>
<meta charset="utf-8">
<title>Tarvel Plumbing Solutions – Flyer</title>
<link href="https://fonts.googleapis.com/css2?family=Arimo:wght@400;700&family=Noto+Sans:wght@400&display=swap" rel="stylesheet">
<style>
  :root{
    --navy:#1f2d4f;
    --band-blue:#4f95d0;
    --orange:#f26a1b;
    --badge-orange:#f0742a;
    --icon-blue:#3a98da;
    --ink:#1b1b1b;
    --heading-ink:#1f2d4f;
    --white:#ffffff;
    --divider:#bdbdbd;
    --mascot-light:#dfe6ef;
    --mascot-mid:#9fb2c9;
  }
  *{margin:0;padding:0;box-sizing:border-box}
  html,body{width:850px;height:1200px;overflow:hidden;background:var(--white)}
  body{font-family:"Arimo",Arial,sans-serif;color:var(--ink)}
  .flyer{position:relative;width:850px;height:1200px;overflow:hidden;background:var(--white)}

  .masthead{position:absolute;left:0;top:0;width:850px;height:263px;background:var(--navy)}
  .brand-mascot{position:absolute;left:84px;top:30px;width:112px;height:200px;border-radius:40px;background:linear-gradient(180deg,var(--mascot-light),var(--mascot-mid))}
  .brand-name{position:absolute;left:212px;top:112px;color:var(--white);font-weight:700;line-height:1}
  .brand-name .word{display:block;font-size:68px;letter-spacing:1px}
  .brand-name .sub{display:block;font-size:22px;margin-top:8px;letter-spacing:.5px}

  .offer-badge{position:absolute;left:572px;top:22px;width:230px;height:230px}
  .offer-text{position:absolute;left:572px;top:22px;width:230px;height:230px;display:flex;flex-direction:column;align-items:center;justify-content:center;color:var(--white);text-align:center;font-size:22px;line-height:1.3}
  .offer-text .pct{font-size:38px;font-weight:700;line-height:1.15}

  .tagline{position:absolute;left:0;top:263px;width:850px;height:80px;background:var(--band-blue);display:flex;flex-direction:column;justify-content:center;align-items:center;font-size:25px;line-height:1.3;color:var(--ink)}
  .tagline b{font-weight:700}
  .rule{position:absolute;left:0;width:850px;height:11px;background:var(--orange)}
  .rule.top{top:343px}
  .rule.bottom{top:998px}

  .services-title{position:absolute;left:0;top:368px;width:850px;text-align:center;font-family:"Noto Sans",Arial,sans-serif;font-weight:400;font-size:32px;color:var(--heading-ink)}
  .col-divider{position:absolute;top:402px;width:2px;height:568px;background:var(--divider)}
  .col-divider.left{left:269px}
  .col-divider.right{left:582px}

  .service{position:absolute;width:230px;text-align:center}
  .service h3{font-size:26px;font-weight:700;line-height:1.2;color:var(--ink)}
  .service svg{display:block;margin:0 auto}

  .contact{position:absolute;left:0;top:1009px;width:850px;height:191px;background:var(--band-blue)}
  .contact-line{position:absolute;left:56px;display:flex;align-items:center;font-size:25px;font-weight:700;color:var(--ink)}
  .contact-line svg{width:38px;height:38px;margin-right:16px}
  .social-tiles{position:absolute;left:727px;top:1121px;display:flex;gap:4px}
  .social-tiles span{width:42px;height:42px;background:var(--navy);border-radius:4px;display:block}
</style>
</head>
<body>
<main class="flyer">

  <header class="masthead">
    <div class="brand-mascot" role="img" aria-label="Brand mascot illustration holding a pipe wrench"></div>
    <div class="brand-name"><span class="word">TARVEL</span><span class="sub">PLUMBING SOLUTIONS</span></div>

    <svg class="offer-badge" viewBox="0 0 230 230" aria-hidden="true">
      <polygon fill="var(--badge-orange)" points="115,0 126,22 143,4 149,28 170,14 170,39 194,31 187,55 213,53 200,75 225,82 206,97 230,115 206,133 225,148 200,155 213,177 187,175 194,199 170,191 170,216 149,202 143,226 126,208 115,230 104,208 87,226 81,202 60,216 60,191 36,199 43,175 17,177 30,155 5,148 24,133 0,115 24,97 5,82 30,75 17,53 43,55 36,31 60,39 60,14 81,28 87,4 104,22"/>
      <circle cx="115" cy="115" r="90" fill="none" stroke="var(--navy)" stroke-width="4"/>
    </svg>
    <div class="offer-text">
      <span>Mention this<br>flyer to receive</span>
      <span class="pct">15%</span>
      <span>DISCOUNT</span>
    </div>
  </header>

  <section class="tagline">
    <span>Your local reliable Sydney plumber - Specialising</span>
    <span>in all aspects of <b>Plumbing, Drainage &amp; Gas Maintenance.</b></span>
  </section>
  <div class="rule top"></div>

  <h2 class="services-title">Ours services:</h2>
  <div class="col-divider left"></div>
  <div class="col-divider right"></div>

  <div class="service" style="left:46px;top:426px">
    <h3>Emergency<br>plumbing</h3>
    <svg width="86" height="86" viewBox="0 0 86 86" style="margin-top:20px" aria-hidden="true">
      <circle cx="46" cy="40" r="34" fill="none" stroke="var(--icon-blue)" stroke-width="2.5" stroke-dasharray="5 4"/>
      <path d="M12 16c6-6 12-4 14 2l3 9c1 4-2 6-5 7 2 8 8 15 16 18 1-3 4-6 8-4l8 4c5 2 6 9 0 14-8 7-26 2-38-12C8 40 5 24 12 16z" fill="var(--icon-blue)"/>
      <text x="48" y="47" text-anchor="middle" font-family="Arimo,sans-serif" font-weight="700" font-size="26" fill="var(--icon-blue)">24</text>
    </svg>
  </div>
  <div class="service" style="left:312px;top:426px">
    <h3>Plumbing<br>maintenance</h3>
    <svg width="90" height="86" viewBox="0 0 90 86" style="margin-top:20px" aria-hidden="true">
      <circle cx="22" cy="20" r="8" fill="var(--icon-blue)"/>
      <path d="M12 32h16l8 18 10-6 3 5-14 10-7-10v24H10l4-20-8 4-3-5z" fill="var(--icon-blue)"/>
      <rect x="50" y="34" width="32" height="20" rx="3" fill="var(--icon-blue)"/>
      <path d="M66 6v14h-8v-5h4V6z" fill="var(--icon-blue)"/>
      <rect x="72" y="8" width="12" height="26" fill="var(--icon-blue)"/>
      <line x1="66" y1="58" x2="66" y2="66" stroke="var(--icon-blue)" stroke-width="3"/>
      <line x1="74" y1="58" x2="74" y2="64" stroke="var(--icon-blue)" stroke-width="3"/>
    </svg>
  </div>
  <div class="service" style="left:573px;top:426px">
    <h3>Drainage<br>maintenance</h3>
    <svg width="86" height="90" viewBox="0 0 86 90" style="margin-top:20px" aria-hidden="true">
      <rect x="4" y="6" width="22" height="8" fill="var(--icon-blue)"/>
      <rect x="56" y="6" width="22" height="8" fill="var(--icon-blue)"/>
      <path d="M8 16h14v18a19 19 0 0 0 38 0V16h14v18a33 33 0 0 1-66 0z" fill="var(--icon-blue)"/>
      <path d="M41 68c3 6 5 8 5 11a5 5 0 0 1-10 0c0-3 2-5 5-11z" fill="var(--icon-blue)"/>
    </svg>
  </div>

  <div class="service" style="left:46px;top:625px">
    <h3>Gas<br>maintenance</h3>
    <svg width="60" height="76" viewBox="0 0 60 76" style="margin-top:22px" aria-hidden="true">
      <path d="M30 2C36 20 56 30 56 50a26 26 0 0 1-52 0C4 34 18 26 30 2z" fill="var(--icon-blue)"/>
      <path d="M30 40c5 8 12 12 12 20a12 12 0 0 1-24 0c0-7 7-11 12-20z" fill="#fff"/>
    </svg>
  </div>
  <div class="service" style="left:312px;top:618px">
    <h3>Hot water<br>systems</h3>
    <svg width="50" height="84" viewBox="0 0 50 84" style="margin-top:20px" aria-hidden="true">
      <rect x="2" y="2" width="46" height="72" rx="6" fill="var(--icon-blue)"/>
      <circle cx="25" cy="20" r="4" fill="none" stroke="#fff" stroke-width="2"/>
      <circle cx="25" cy="32" r="4" fill="none" stroke="#fff" stroke-width="2"/>
      <rect x="15" y="48" width="20" height="10" rx="2" fill="none" stroke="#fff" stroke-width="2"/>
      <rect x="14" y="76" width="5" height="6" fill="var(--icon-blue)"/>
      <rect x="31" y="76" width="5" height="6" fill="var(--icon-blue)"/>
    </svg>
  </div>
  <div class="service" style="left:573px;top:625px">
    <h3>Leaking<br>fixtures</h3>
    <svg width="80" height="56" viewBox="0 0 80 56" style="margin-top:38px" aria-hidden="true">
      <rect x="0" y="20" width="28" height="8" fill="var(--icon-blue)"/>
      <rect x="34" y="14" width="44" height="20" fill="var(--icon-blue)"/>
      <rect x="52" y="4" width="6" height="10" fill="var(--icon-blue)"/>
      <rect x="44" y="2" width="22" height="4" fill="var(--icon-blue)"/>
      <path d="M34 34v10h10V34z" fill="var(--icon-blue)"/>
      <path d="M39 46c2 4 3 5 3 7a3 3 0 0 1-6 0c0-2 1-3 3-7z" fill="var(--icon-blue)"/>
    </svg>
  </div>

  <div class="service" style="left:46px;top:819px">
    <h3>Blocked sewer<br>&amp; stormwater</h3>
    <svg width="96" height="56" viewBox="0 0 96 56" style="margin-top:22px" aria-hidden="true">
      <path d="M2 30l12-6v12z" fill="var(--icon-blue)"/>
      <rect x="18" y="22" width="16" height="16" fill="var(--icon-blue)"/>
      <circle cx="56" cy="32" r="20" fill="var(--icon-blue)"/>
      <circle cx="56" cy="32" r="11" fill="none" stroke="#fff" stroke-width="2"/>
      <path d="M70 6h22v8h-8v18a22 22 0 0 1-8 16l-6-6a14 14 0 0 0 6-10V14h-6z" fill="var(--icon-blue)"/>
    </svg>
  </div>
  <div class="service" style="left:312px;top:813px">
    <h3>Camera &amp;<br>locating</h3>
    <svg width="80" height="80" viewBox="0 0 80 80" style="margin-top:20px" aria-hidden="true">
      <path d="M4 22a50 50 0 0 1 72 0" fill="none" stroke="var(--icon-blue)" stroke-width="5" stroke-linecap="round"/>
      <path d="M15 34a34 34 0 0 1 50 0" fill="none" stroke="var(--icon-blue)" stroke-width="5" stroke-linecap="round"/>
      <path d="M26 46a18 18 0 0 1 28 0" fill="none" stroke="var(--icon-blue)" stroke-width="5" stroke-linecap="round"/>
      <circle cx="40" cy="64" r="9" fill="none" stroke="var(--icon-blue)" stroke-width="5"/>
      <rect x="37" y="50" width="6" height="5" fill="var(--icon-blue)"/>
      <rect x="37" y="73" width="6" height="5" fill="var(--icon-blue)"/>
    </svg>
  </div>
  <div class="service" style="left:573px;top:819px">
    <h3>TMV<br>maintenance</h3>
    <svg width="64" height="82" viewBox="0 0 64 82" style="margin-top:18px" aria-hidden="true">
      <path d="M26 4C34 22 48 34 48 52a22 22 0 0 1-44 0C4 34 18 22 26 4z" fill="none" stroke="var(--icon-blue)" stroke-width="4"/>
      <rect x="40" y="30" width="12" height="36" rx="6" fill="#fff" stroke="var(--icon-blue)" stroke-width="4"/>
      <circle cx="46" cy="70" r="9" fill="var(--icon-blue)"/>
      <rect x="44" y="44" width="4" height="24" fill="var(--icon-blue)"/>
    </svg>
  </div>

  <div class="rule bottom"></div>

  <footer class="contact">
    <div class="contact-line" style="top:30px">
      <svg viewBox="0 0 38 38" aria-hidden="true"><path d="M7 4c3-2 6-1 7 2l2 6c1 2-1 4-3 5 2 5 5 8 9 10 1-2 3-4 5-3l6 2c3 1 4 4 2 7-5 5-14 3-22-5S2 9 7 4z" fill="none" stroke="var(--ink)" stroke-width="2"/></svg>
      <span>0400 555 218</span>
    </div>
    <div class="contact-line" style="top:78px">
      <svg viewBox="0 0 38 38" aria-hidden="true"><circle cx="19" cy="19" r="16" fill="none" stroke="var(--ink)" stroke-width="2"/><path d="M12 19h14a7 7 0 1 0-2 6" fill="none" stroke="var(--ink)" stroke-width="2"/></svg>
      <span>tarvelplumbingsolutions@mailhub.com</span>
    </div>
    <div class="contact-line" style="top:131px">
      <svg viewBox="0 0 38 38" aria-hidden="true"><rect x="4" y="4" width="30" height="30" rx="3" fill="none" stroke="var(--ink)" stroke-width="2"/></svg>
      <span>@TarvelPlumbingSolutions</span>
    </div>
  </footer>
  <div class="social-tiles"><span></span><span></span></div>

</main>
</body>
</html>
```